Mend and secure Word doc project

Mend & Secure are an established home appliance repair and warranty provider looking to rebrand the letters sent to our customers with a new and fresh design.
Please refer to our website for our colour scheme and logo which we are not looking to change:
www.mendandsecure.co.uk
The letters which we are looking to have redesigned are:
Welcome letters / confirmation paperwork
Basic letter template
Welcome letters:
Page 1 – Opening / Welcome
Page 2 – Plan documentation details
Page 3 & 4 – Terms & Conditions
We can provide a copy of our current welcome / confirmation letters but as we are looking for full redesign, we are looking to steer away from what we have been using historically.
We will be running further projects and we are looking to use the same designer which we pick from this competition so please consider this when submitting your designs.
UPDATE - 01/11/23
An example of our current Welcome documentation has been uploaded for the purpose of example of the placement of the content. As per the brief, we are not looking for a similar design but purely uploading the current documentation to give you an idea of what we are currently using.
Look and feel
Each slider illustrates characteristics of the customer's brand and the style your logo design should communicate.

```html
<!DOCTYPE html>
<html lang="en">
<head>
<meta charset="utf-8">
<title>Mend &amp; Secure – Letter Suite</title>
<link rel="stylesheet" href="https://fonts.googleapis.com/css2?family=Montserrat:wght@400;500;600;700&family=Great+Vibes&family=Roboto:wght@400&display=swap">
<style>
:root{
  --bg:#e8e8e8;
  --paper:#ffffff;
  --teal:#1a88aa;
  --green:#a7e08b;
  --green-text:#6cb857;
  --heading-blue:#1f85b2;
  --rule-green:#8fca78;
  --ink:#222;
  --body:#444;
  --row-grey:#efefef;
  --caption:#444;
  --grad:linear-gradient(90deg,var(--teal) 0%,#5fb3a0 55%,var(--green) 100%);
  --grad-rev:linear-gradient(90deg,var(--green) 0%,#5fb3a0 45%,var(--teal) 100%);
}
*{margin:0;padding:0;box-sizing:border-box}
html,body{width:1200px;height:2609px;overflow:hidden}
body{background:var(--bg);position:relative;font-family:'Montserrat',sans-serif;color:var(--body)}
.page{position:absolute;background:var(--paper);box-shadow:0 2px 10px rgba(0,0,0,.12);overflow:hidden}
.abs{position:absolute}
.caption{position:absolute;font-family:'Roboto',sans-serif;font-size:44px;color:var(--caption);white-space:nowrap}
.body-text{font-size:8px;line-height:11.6px;color:var(--body)}
.body-text p+p{margin-top:11px}

/* company name, set plainly in the body face */
.company-name{font-family:'Montserrat',sans-serif;font-weight:600;letter-spacing:0;white-space:nowrap}

/* welcome page */
.welcome{left:62px;top:63px;width:500px;height:707px}
.welcome .photo{left:0;top:44px;width:500px;height:218px;background:linear-gradient(100deg,#cfc6ba 0%,#a99a88 35%,#e2ddd6 60%,#8f8a86 100%)}
.welcome .brand-panel{left:271px;top:0;width:214px;height:210px;background:linear-gradient(180deg,rgba(165,220,180,.95) 0%,rgba(40,155,175,.92) 100%);display:flex;align-items:center;justify-content:center}
.welcome .company-name{color:#fff;font-size:18px}
.welcome .greeting{left:20px;top:276px;font-family:'Great Vibes',cursive;font-size:34px;font-weight:400;color:var(--green-text);white-space:nowrap}
.welcome .salutation{left:46px;top:334px;font-size:9px;font-weight:600;color:var(--ink)}
.welcome .letter-body{left:46px;top:356px;width:400px}
.signature{background:linear-gradient(90deg,#eee,#d8d8d8);border-radius:3px}
.welcome .signature{left:368px;top:546px;width:76px;height:20px}
.welcome .signer{left:336px;top:570px;font-size:9px;font-weight:600;color:var(--ink)}
.footer-rule{height:2px;background:linear-gradient(90deg,var(--teal) 0 50%,var(--rule-green) 50% 100%)}
.welcome .footer-rule{left:33px;top:605px;width:426px}
.contact-addr{font-size:9px;line-height:11.5px;color:var(--ink)}
.contact-addr b{font-weight:700}
.contact-line{display:flex;align-items:center;gap:6px;font-size:9px;line-height:14px;color:var(--ink)}
.contact-line svg{width:10px;height:10px;fill:var(--ink)}
.welcome .contact-addr{left:47px;top:624px}
.welcome .contacts{left:279px;top:626px}
.band-bottom{height:34px}
.welcome .band-bottom{left:0;bottom:0;width:500px;background:var(--grad)}

/* plan documentation */
.plan{left:633px;top:63px;width:497px;height:702px}
.plan .header{left:0;top:0;width:497px;height:90px;background:var(--grad)}
.plan .title{left:58px;top:26px;color:#fff;font-size:21px;line-height:23px}
.plan .title b{font-weight:700;display:block}
.plan .title span{font-weight:400}
.plan .title-mark{left:41px;top:70px;width:11px;height:11px;background:#fff}
.plan-row{position:absolute;left:0;width:497px;display:flex;align-items:center}
.plan-row.alt{background:var(--row-grey)}
.plan-row h3{width:192px;padding-left:44px;font-size:14.5px;line-height:18px;font-weight:600;color:var(--green-text)}
.plan-row .body-text{width:275px;font-size:7.8px;line-height:11.4px}
.plan .end-rule{left:50px;top:682px;width:397px;height:2px;background:var(--rule-green)}

/* terms */
.terms-a{left:62px;top:883px;width:498px;height:705px}
.terms-b{left:633px;top:887px;width:494px;height:696px}
.terms-a .head-band{left:0;top:37px;width:214px;height:28px;background:var(--grad-rev)}
.terms-a .title{left:224px;top:40px;font-size:18px;line-height:19px;font-weight:700;color:var(--heading-blue)}
.terms-b .head-band{left:37px;top:34px;width:457px;height:26px;background:var(--grad)}
.clauses{position:absolute;display:flex;flex-direction:column}
.clause{border-top:2px solid var(--rule-green);padding-top:9px}
.clause h4{font-size:11.5px;font-weight:700;color:var(--ink);margin-bottom:6px}
.clause .body-text{font-size:6.4px;line-height:9.7px}
.clause .body-text p+p{margin-top:9px}
.terms-a .clauses{left:36px;top:110px;width:422px;gap:20px}
.terms-a .clause{height:92px}
.terms-b .clauses{left:37px;top:66px;width:420px;gap:0}
.terms-b .clause{height:91px}
.terms-a .band-bottom{left:126px;top:649px;width:372px;height:26px;background:var(--grad)}
.terms-b .band-bottom{left:0;top:641px;width:464px;height:25px;background:var(--grad)}

/* basic letter */
.letter{left:354px;top:1703px;width:492px;height:697px}
.letter .brand{left:40px;top:56px}
.letter .company-name{color:var(--teal);font-size:13px}
.letter .top-rule{left:34px;top:92px;width:422px;height:2px;background:linear-gradient(90deg,var(--rule-green) 0 35%,var(--teal) 35% 100%)}
.letter .recipient{left:41px;top:110px;font-size:8px;line-height:9.6px;color:var(--body)}
.letter .recipient b{display:block;font-size:9.5px;color:var(--ink);font-weight:700;margin-bottom:1px}
.letter .date{left:341px;top:126px;font-size:8.5px;font-weight:600;color:var(--ink)}
.letter .subject{left:0;width:492px;top:174px;text-align:center;font-size:8.5px;font-weight:700;color:var(--ink)}
.letter .letter-body{left:41px;top:202px;width:400px}
.letter .signature{left:362px;top:510px;width:78px;height:20px}
.letter .signer{left:378px;top:532px;font-size:9px;line-height:10px;font-weight:600;color:var(--ink);text-align:right}
.letter .footer-rule{left:34px;top:596px;width:418px}
.letter .contact-addr{left:47px;top:614px}
.letter .contacts{left:274px;top:617px}
.letter .band-bottom{left:0;bottom:0;width:492px;height:26px;background:var(--grad-rev)}
</style>
</head>
<body>

<!-- Page 1: Welcome letter -->
<section class="page welcome">
  <div class="abs photo" role="img" aria-label="Photograph of a modern kitchen with built-in ovens and a sink"></div>
  <div class="abs brand-panel">
    <span class="company-name">Mend &amp; Secure</span>
  </div>
  <h1 class="abs greeting">Welcome, Esteemed Customer</h1>
  <p class="abs salutation">Dear [Client],</p>
  <div class="abs letter-body body-text">
    <p>Lorem ipsum dolor sit amet, consectetur adipiscing elit. Nullam eget justo eu justo eleifend rhoncus. Sed auctor quam non urna vehicula, ac tincidunt neque scelerisque. Phasellus commodo augue at mi varius, id luctus mi bibendum. Nullam et felis in nunc euismod dignissim. Integer et arcu in risus bibendum lacinia.</p>
    <p>Consectetur adipiscing elit. Nullam eget justo eu justo eleifend rhoncus. Sed auctor quam non urna vehicula, ac tincidunt neque scelerisque. Phasellus commodo augue at mi varius, id luctus mi bibendum. Nullam et felis in nunc euismod dignissim. Integer et arcu in risus bibendum lacinia.</p>
    <p>Vestibulum fringilla odio nec libero malesuada, id bibendum libero egestas. Suspendisse at dolor nec purus rhoncus laoreet. Proin vestibulum, odio ac luctus accumsan, ipsum lorem tempus odio, in tincidunt augue nunc ut felis. Curabitur id sollicitudin elit. Sed ut turpis vel risus ultricies vehicula a non lectus. Vivamus auctor lacus a bibendum aliquet. Sed auctor euismod libero, eget vulputate dui feugiat eu. Sed eget ex id elit volutpat pellentesque. Sed in augue nec erat varius bibendum.</p>
  </div>
  <div class="abs signature" role="img" aria-label="Handwritten signature"></div>
  <p class="abs signer">Alan Webb, Manager</p>
  <div class="abs footer-rule"></div>
  <p class="abs contact-addr"><b>Mend &amp; Secure LTD,</b><br>Harbour House First Floor, 14 West<br>Street Seaford BN9 2AB</p>
  <div class="abs contacts">
    <p class="contact-line"><svg viewBox="0 0 24 24"><path d="M6.6 10.8a15 15 0 0 0 6.6 6.6l2.2-2.2c.3-.3.7-.4 1-.2 1.1.4 2.3.6 3.6.6.6 0 1 .4 1 1V20c0 .6-.4 1-1 1A17 17 0 0 1 3 4c0-.6.4-1 1-1h3.5c.6 0 1 .4 1 1 0 1.3.2 2.5.6 3.6.1.3 0 .7-.2 1z"/></svg>0800 146 2270</p>
    <p class="contact-line"><svg viewBox="0 0 24 24"><path d="M2 5h20v14H2zm2 2v.5l8 5 8-5V7zm0 2.8V17h16V9.8l-8 5z"/></svg>support@mendandsecure.com</p>
  </div>
  <div class="abs band-bottom"></div>
</section>
<p class="caption" style="left:75px;top:782px">page 1 - welcome letter</p>

<!-- Page 2: Plan documentation -->
<section class="page plan">
  <div class="abs header"></div>
  <h2 class="abs title"><b>PLAN DOCUMENTATION</b><span>DETAILS</span></h2>
  <div class="abs title-mark"></div>
  <div class="plan-row" style="top:90px;height:165px">
    <h3>Lorem<br>ipsum dolor<br>Consectetur<br>adipiscing elit.</h3>
    <div class="body-text"><p>Lorem ipsum dolor sit amet, consectetur adipiscing elit. Nullam eget justo eu justo eleifend rhoncus. Sed auctor quam non urna vehicula, ac tincidunt neque scelerisque. Phasellus commodo augue at mi varius, id luctus mi bibendum. Nullam et felis in nunc euismod dignissim. Integer et arcu in risus bibendum lacinia.</p><p>Consectetur adipiscing elit. Nullam eget justo eu justo eleifend rhoncus. Sed auctor quam non urna vehicula</p></div>
  </div>
  <div class="plan-row alt" style="top:257px;height:160px">
    <h3>Consectetur<br>adipiscing elit.</h3>
    <div class="body-text"><p>Lorem ipsum dolor sit amet, consectetur adipiscing elit. Nullam eget justo eu justo eleifend rhoncus. Sed auctor quam non urna vehicula, ac tincidunt neque scelerisque. Phasellus commodo augue at mi varius, id luctus mi bibendum. Nullam et felis in nunc euismod dignissim. Integer et arcu in risus bibendum lacinia.</p><p>Consectetur adipiscing elit. Nullam eget justo eu justo eleifend rhoncus. Sed auctor quam non urna vehicula</p></div>
  </div>
  <div class="plan-row" style="top:417px;height:130px">
    <h3>Sed auctor<br>quam non urna<br>vehicula</h3>
    <div class="body-text"><p>Lorem ipsum dolor sit amet, consectetur adipiscing elit. Nullam eget justo eu justo eleifend rhoncus. Sed auctor quam non urna vehicula, ac tincidunt neque scelerisque. Phasellus commodo augue at mi varius, id luctus mi bibendum. Nullam eget justo eu justo eleifend rhoncus. Sed auctor quam non urna vehicula, ac tincidunt neque scelerisque. Phasellus commodo augue at mi varius</p></div>
  </div>
  <div class="plan-row alt" style="top:547px;height:122px">
    <h3>Lorem<br>ipsum dolor<br>Consectetur<br>adipiscing elit.</h3>
    <div class="body-text"><p>Lorem ipsum dolor sit amet, consectetur adipiscing elit. Nullam eget justo eu justo eleifend rhoncus. Sed auctor quam non urna vehicula, ac tincidunt neque scelerisque. Phasellus commodo augue at mi varius, id luctus mi bibendum. Nullam et felis in nunc euismod dignissim. Integer et arcu in risus bibendum lacinia.</p></div>
  </div>
  <div class="abs end-rule"></div>
</section>
<p class="caption" style="left:608px;top:780px">page 2 - Plan documentation</p>

<!-- Page 3: Terms & Conditions -->
<section class="page terms-a">
  <div class="abs head-band"></div>
  <h2 class="abs title">TERMS &amp;<br>CONDITIONS</h2>
  <div class="clauses">
    <article class="clause"><h4>Consectetur adipiscing elit.</h4><div class="body-text"><p>Lorem ipsum dolor sit amet, consectetur adipiscing elit. Nullam eget justo eu justo eleifend rhoncus. Sed auctor quam non urna vehicula, ac tincidunt neque scelerisque. Phasellus commodo augue at mi varius, id luctus mi bibendum. Nullam et felis in nunc euismod dignissim. Integer et arcu in risus bibendum lacinia.</p><p>Consectetur adipiscing elit. Nullam eget justo eu justo eleifend rhoncus. Sed auctor quam non urna vehicula</p></div></article>
    <article class="clause"><h4>Nullam et felis in nunc euismod dignissim.</h4><div class="body-text"><p>Lorem ipsum dolor sit amet, consectetur adipiscing elit. Nullam eget justo eu justo eleifend rhoncus. Sed auctor quam non urna vehicula, ac tincidunt neque scelerisque. Phasellus commodo augue at mi varius, id luctus mi bibendum. Nullam et felis in nunc euismod dignissim. Integer et arcu in risus bibendum lacinia.</p><p>Consectetur adipiscing elit. Nullam eget justo eu justo eleifend rhoncus. Sed auctor quam non urna vehicula</p></div></article>
    <article class="clause"><h4>Consectetur adipiscing elit.</h4><div class="body-text"><p>Lorem ipsum dolor sit amet, consectetur adipiscing elit. Nullam eget justo eu justo eleifend rhoncus. Sed auctor quam non urna vehicula, ac tincidunt neque scelerisque. Phasellus commodo augue at mi varius, id luctus mi bibendum. Nullam et felis in nunc euismod dignissim. Integer et arcu in risus bibendum lacinia.</p><p>Consectetur adipiscing elit. Nullam eget justo eu justo eleifend rhoncus. Sed auctor quam non urna vehicula</p></div></article>
    <article class="clause"><h4>Nullam et felis in nunc euismod dignissim.</h4><div class="body-text"><p>Lorem ipsum dolor sit amet, consectetur adipiscing elit. Nullam eget justo eu justo eleifend rhoncus. Sed auctor quam non urna vehicula, ac tincidunt neque scelerisque. Phasellus commodo augue at mi varius, id luctus mi bibendum. Nullam et felis in nunc euismod dignissim. Integer et arcu in risus bibendum lacinia.</p><p>Consectetur adipiscing elit. Nullam eget justo eu justo eleifend rhoncus. Sed auctor quam non urna vehicula</p></div></article>
    <article class="clause"><h4>Consectetur adipiscing elit.</h4><div class="body-text"><p>Lorem ipsum dolor sit amet, consectetur adipiscing elit. Nullam eget justo eu justo eleifend rhoncus. Sed auctor quam non urna vehicula, ac tincidunt neque scelerisque. Phasellus commodo augue at mi varius, id luctus mi bibendum. Nullam et felis in nunc euismod dignissim. Integer et arcu in risus bibendum lacinia.</p><p>Consectetur adipiscing elit. Nullam eget justo eu justo eleifend rhoncus. Sed auctor quam non urna vehicula</p></div></article>
  </div>
  <div class="abs band-bottom"></div>
</section>

<!-- Page 4: Terms & Conditions continued -->
<section class="page terms-b">
  <div class="abs head-band"></div>
  <div class="clauses">
    <article class="clause"><h4>Consectetur adipiscing elit.</h4><div class="body-text"><p>Lorem ipsum dolor sit amet, consectetur adipiscing elit. Nullam eget justo eu justo eleifend rhoncus. Sed auctor quam non urna vehicula, ac tincidunt neque scelerisque. Phasellus commodo augue at mi varius, id luctus mi bibendum. Nullam et felis in nunc euismod dignissim. Integer et arcu in risus bibendum lacinia.</p><p>Consectetur adipiscing elit. Nullam eget justo eu justo eleifend rhoncus. Sed auctor quam non urna vehicula</p></div></article>
    <article class="clause"><h4>Nullam et felis in nunc euismod dignissim.</h4><div class="body-text"><p>Lorem ipsum dolor sit amet, consectetur adipiscing elit. Nullam eget justo eu justo eleifend rhoncus. Sed auctor quam non urna vehicula, ac tincidunt neque scelerisque. Phasellus commodo augue at mi varius, id luctus mi bibendum. Nullam et felis in nunc euismod dignissim. Integer et arcu in risus bibendum lacinia.</p><p>Consectetur adipiscing elit. Nullam eget justo eu justo eleifend rhoncus. Sed auctor quam non urna vehicula</p></div></article>
    <article class="clause"><h4>Consectetur adipiscing elit.</h4><div class="body-text"><p>Lorem ipsum dolor sit amet, consectetur adipiscing elit. Nullam eget justo eu justo eleifend rhoncus. Sed auctor quam non urna vehicula, ac tincidunt neque scelerisque. Phasellus commodo augue at mi varius, id luctus mi bibendum. Nullam et felis in nunc euismod dignissim. Integer et arcu in risus bibendum lacinia.</p><p>Consectetur adipiscing elit. Nullam eget justo eu justo eleifend rhoncus. Sed auctor quam non urna vehicula</p></div></article>
    <article class="clause"><h4>Nullam et felis in nunc euismod dignissim.</h4><div class="body-text"><p>Lorem ipsum dolor sit amet, consectetur adipiscing elit. Nullam eget justo eu justo eleifend rhoncus. Sed auctor quam non urna vehicula, ac tincidunt neque scelerisque. Phasellus commodo augue at mi varius, id luctus mi bibendum. Nullam et felis in nunc euismod dignissim. Integer et arcu in risus bibendum lacinia.</p><p>Consectetur adipiscing elit. Nullam eget justo eu justo eleifend rhoncus. Sed auctor quam non urna vehicula</p></div></article>
    <article class="clause"><h4>Consectetur adipiscing elit.</h4><div class="body-text"><p>Lorem ipsum dolor sit amet, consectetur adipiscing elit. Nullam eget justo eu justo eleifend rhoncus. Sed auctor quam non urna vehicula, ac tincidunt neque scelerisque. Phasellus commodo augue at mi varius, id luctus mi bibendum. Nullam et felis in nunc euismod dignissim. Integer et arcu in risus bibendum lacinia.</p><p>Consectetur adipiscing elit. Nullam eget justo eu justo eleifend rhoncus. Sed auctor quam non urna vehicula</p></div></article>
    <article class="clause"><h4>Consectetur adipiscing elit.</h4><div class="body-text"><p>Lorem ipsum dolor sit amet, consectetur adipiscing elit. Nullam eget justo eu justo eleifend rhoncus. Sed auctor quam non urna vehicula, ac tincidunt neque scelerisque. Phasellus commodo augue at mi varius, id luctus mi bibendum. Nullam et felis in nunc euismod dignissim. Integer et arcu in risus bibendum lacinia.</p><p>Consectetur adipiscing elit. Nullam eget justo eu justo eleifend rhoncus. Sed auctor quam non urna vehicula</p></div></article>
  </div>
  <div class="abs band-bottom"></div>
</section>
<p class="caption" style="left:0;width:1200px;text-align:center;top:1612px">Page 3 - 4 Terms and Conditions</p>

<!-- Basic letter template -->
<section class="page letter">
  <div class="abs brand"><span class="company-name">Mend &amp; Secure</span></div>
  <div class="abs top-rule"></div>
  <p class="abs recipient"><b>To Alan Webb</b>Managing Director,<br>Webb Enterprises,<br>8, Mill Lane, Anytown.</p>
  <p class="abs date">15th October, 2023</p>
  <p class="abs subject">LOREM IPSUM DOLOR SIT AMET</p>
  <div class="abs letter-body body-text">
    <p>Lorem ipsum dolor sit amet, consectetur adipiscing elit. Nullam eget justo eu justo eleifend rhoncus. Sed auctor quam non urna vehicula, ac tincidunt neque scelerisque. Phasellus commodo augue at mi varius, id luctus mi bibendum. Nullam et felis in nunc euismod dignissim. Integer et arcu in risus bibendum lacinia.</p>
    <p>Consectetur adipiscing elit. Nullam eget justo eu justo eleifend rhoncus. Sed auctor quam non urna vehicula, ac tincidunt neque scelerisque. Phasellus commodo augue at mi varius, id luctus mi bibendum. Nullam et felis in nunc euismod dignissim. Integer et arcu in risus bibendum lacinia.</p>
    <p>Vestibulum fringilla odio nec libero malesuada, id bibendum libero egestas. Suspendisse at dolor nec purus rhoncus laoreet. Proin vestibulum, odio ac luctus accumsan, ipsum lorem tempus odio, in tincidunt augue nunc ut felis. Curabitur id sollicitudin elit. Sed ut turpis vel risus ultricies vehicula a non lectus. Vivamus auctor lacus a bibendum aliquet. Sed auctor euismod libero, eget vulputate dui feugiat eu. Sed eget ex id elit volutpat pellentesque. Sed in augue nec erat varius bibendum.</p>
    <p>Consectetur adipiscing elit. Nullam eget justo eu justo eleifend rhoncus. Sed auctor quam non urna vehicula, ac tincidunt neque scelerisque. Phasellus commodo augue at mi varius, id luctus mi bibendum. Nullam et felis in nunc euismod dignissim.</p>
    <p>Consectetur adipiscing elit. Nullam eget justo eu justo eleifend rhoncus. Sed auctor quam non urna vehicula, ac tincidunt neque scelerisque. Phasellus commodo augue at mi varius, id luctus mi bibendum. Nullam et felis in nunc euismod dignissim.</p>
  </div>
  <div class="abs signature" role="img" aria-label="Handwritten signature"></div>
  <p class="abs signer">Alan Webb<br>Manager</p>
  <div class="abs footer-rule"></div>
  <p class="abs contact-addr"><b>Mend &amp; Secure LTD,</b><br>Harbour House First Floor, 14 West<br>Street Seaford BN9 2AB</p>
  <div class="abs contacts">
    <p class="contact-line"><svg viewBox="0 0 24 24"><path d="M6.6 10.8a15 15 0 0 0 6.6 6.6l2.2-2.2c.3-.3.7-.4 1-.2 1.1.4 2.3.6 3.6.6.6 0 1 .4 1 1V20c0 .6-.4 1-1 1A17 17 0 0 1 3 4c0-.6.4-1 1-1h3.5c.6 0 1 .4 1 1 0 1.3.2 2.5.6 3.6.1.3 0 .7-.2 1z"/></svg>0800 146 2270</p>
    <p class="contact-line"><svg viewBox="0 0 24 24"><path d="M2 5h20v14H2zm2 2v.5l8 5 8-5V7zm0 2.8V17h16V9.8l-8 5z"/></svg>support@mendandsecure.com</p>
  </div>
  <div class="abs band-bottom"></div>
</section>
<p class="caption" style="left:0;width:1200px;text-align:center;top:2432px">Basic Letter Template</p>

</body>
</html>
```